electrical contractor business card for professional modern company

I need a business card design for an electrical contractors business. I do all kinds of electricical work from new homes, air conditioning, data and communications. I have a logo design i want on it and have a good idea in my head of what i want it to look like. I like simple yet bold and professional looking. All black background is a must

Target Market(s)

Anyone needing electrical work done

Industry/Entity Type

Electrical

Contact Information for Business Card

company name- KMP Electrical and Data
person name-lewis pembury
phone number- 0468 239 517
website-kmpwire-sample.com.au

Font styles to use
Sans Serif

Requirements
Must have
• email
• website
• logo
• name
• phone number
• list of work i do:
• -electrical
• -air-conditioning
• -data/communications
• -cctv/security
• -domestic/commercial/industrial
• -24hr emergency breakdown repair
Nice to have
• i would like the logo on the front side in the centre taking up most of the card with black background.
• on the rear i want the list of work i do with company info i.e. email, website, my name, phone number. rear of card also black background with orange writing to match the orange in the logo

```html
<!DOCTYPE html>
<html lang="en">
<head>
<meta charset="utf-8">
<title>KMP Electrical and Data – Business Card</title>
<link href="https://fonts.googleapis.com/css2?family=Open+Sans:wght@400;600&display=swap" rel="stylesheet">
<style>
  :root {
    --stage: #e8e5e1;
    --card: #050505;
    --orange: #f07a2a;
    --grey: #bdbdbd;
    --shadow: rgba(0,0,0,0.25);
  }
  * { margin: 0; padding: 0; box-sizing: border-box; }
  html, body {
    width: 1200px; height: 914px; overflow: hidden;
    background: var(--stage);
    font-family: "Open Sans", Arial, sans-serif;
  }
  .canvas {
    width: 1200px; height: 914px;
    display: flex; flex-direction: column; align-items: center; justify-content: space-evenly;
  }
  .card {
    position: relative;
    width: 700px; height: 400px;
    background: var(--card);
    border-radius: 4px;
    box-shadow: 0 10px 28px var(--shadow);
    overflow: hidden;
  }
  /* Services side */
  .services-title {
    position: absolute; left: 52px; top: 64px;
    color: var(--orange); font-size: 30px; font-weight: 400;
  }
  .service-list {
    position: absolute; left: 52px; top: 146px;
    list-style: none;
  }
  .service-list li {
    display: flex; align-items: center; gap: 14px;
    color: var(--grey); font-size: 19px; line-height: 30px;
  }
  .bullet { width: 16px; height: 16px; flex: none; }
  .brand {
    position: absolute;
    display: flex; align-items: center; gap: 14px;
    color: var(--orange); font-weight: 600;
  }
  .brand-dot {
    width: 22px; height: 22px; border-radius: 50%;
    background: var(--orange); flex: none;
  }
  .brand-name { font-size: 26px; line-height: 1.15; }
  .services-side .brand { right: 52px; top: 150px; }
  /* Contact side */
  .contact-side .brand { left: 44px; top: 158px; }
  .contact-side .brand-name { font-size: 23px; }
  .divider {
    position: absolute; left: 0; top: 0;
  }
  .holder-name {
    position: absolute; left: 420px; top: 118px;
    color: var(--orange); font-size: 36px; font-weight: 400;
    transform: translateX(-10px);
  }
  .contact-list {
    position: absolute; left: 410px; top: 196px;
    list-style: none;
    color: var(--grey); font-size: 19px; line-height: 34px;
  }
</style>
</head>
<body>
<main class="canvas">

  <section class="card services-side" aria-label="Card back: services">
    <h2 class="services-title">service :-</h2>
    <ul class="service-list">
      <li><svg class="bullet" viewBox="0 0 16 16"><circle cx="8" cy="8" r="8" fill="#f07a2a"/><path d="M5 8h6M8.5 5.5 11 8l-2.5 2.5" stroke="#050505" stroke-width="1.8" fill="none" stroke-linecap="round"/></svg>electrical</li>
      <li><svg class="bullet" viewBox="0 0 16 16"><circle cx="8" cy="8" r="8" fill="#f07a2a"/><path d="M5 8h6M8.5 5.5 11 8l-2.5 2.5" stroke="#050505" stroke-width="1.8" fill="none" stroke-linecap="round"/></svg>air-conditioning</li>
      <li><svg class="bullet" viewBox="0 0 16 16"><circle cx="8" cy="8" r="8" fill="#f07a2a"/><path d="M5 8h6M8.5 5.5 11 8l-2.5 2.5" stroke="#050505" stroke-width="1.8" fill="none" stroke-linecap="round"/></svg>data/communications</li>
      <li><svg class="bullet" viewBox="0 0 16 16"><circle cx="8" cy="8" r="8" fill="#f07a2a"/><path d="M5 8h6M8.5 5.5 11 8l-2.5 2.5" stroke="#050505" stroke-width="1.8" fill="none" stroke-linecap="round"/></svg>cctv/security</li>
      <li><svg class="bullet" viewBox="0 0 16 16"><circle cx="8" cy="8" r="8" fill="#f07a2a"/><path d="M5 8h6M8.5 5.5 11 8l-2.5 2.5" stroke="#050505" stroke-width="1.8" fill="none" stroke-linecap="round"/></svg>domestic/commercial/industrial</li>
      <li><svg class="bullet" viewBox="0 0 16 16"><circle cx="8" cy="8" r="8" fill="#f07a2a"/><path d="M5 8h6M8.5 5.5 11 8l-2.5 2.5" stroke="#050505" stroke-width="1.8" fill="none" stroke-linecap="round"/></svg>24hr emergency breakdown repair</li>
    </ul>
    <div class="brand">
      <span class="brand-dot"></span>
      <span class="brand-name">KMP<br>Electrical and Data</span>
    </div>
  </section>

  <section class="card contact-side" aria-label="Card front: contact details">
    <div class="brand">
      <span class="brand-dot"></span>
      <span class="brand-name">KMP<br>Electrical and Data</span>
    </div>
    <svg class="divider" width="700" height="400" viewBox="0 0 700 400" aria-hidden="true">
      <defs>
        <linearGradient id="divider-glow" x1="0" y1="0" x2="0" y2="1">
          <stop offset="0" stop-color="#f07a2a" stop-opacity="0"/>
          <stop offset="0.5" stop-color="#f07a2a" stop-opacity="1"/>
          <stop offset="1" stop-color="#f07a2a" stop-opacity="0"/>
        </linearGradient>
      </defs>
      <line x1="380" y1="40" x2="330" y2="360" stroke="url(#divider-glow)" stroke-width="2"/>
    </svg>
    <h1 class="holder-name">lewis pembury</h1>
    <ul class="contact-list">
      <li>0468 239 517</li>
      <li>kmpwire-sample.com.au</li>
      <li>info@kmpwire-sample.com.au</li>
    </ul>
  </section>

</main>
</body>
</html>
```